Ad campaign in the solar industry

We are a young, up-and-coming solar module production company searching for a new print ad campaign. The design needs to express the core values of our company: a smart product, local support and service, as well as environmental awareness.
We would appreciate designs that communicate the advantages of renewable energy with a strong, clear message. Additionally, the concept should include visually appealing graphics to engage audiences throughout Europe and the US. Design concepts should be drafted in English. The design will appear in many forms; it will be adapted for publications, signage and online campaigns.
We value out-of-the box thinking, a modern approach, and creativity that goes beyond the usual solar ad.

```html
<!DOCTYPE html>
<html lang="en">
<head>
<meta charset="utf-8">
<title>Sunvera – Greener. Smarter. Closer.</title>
<link rel="stylesheet" href="https://fonts.googleapis.com/css2?family=Francois+One&family=Audiowide&family=Arimo:wght@400;700&display=swap">
<style>
  :root {
    --green: #1f7a1f;
    --purple: #7a2a9a;
    --yellow: #fcd21c;
    --orange: #f5a312;
    --sun: #fbd623;
    --brown: #7a3a3a;
    --slate: #565656;
    --grey-band: #c4c4c4;
    --white: #ffffff;
    --ink: #111111;
  }
  * { box-sizing: border-box; margin: 0; padding: 0; }
  html, body { width: 927px; height: 1200px; overflow: hidden; }
  body { font-family: "Arimo", Arial, sans-serif; background: var(--white); }
  .ad { position: relative; width: 927px; height: 1200px; overflow: hidden;
    background: radial-gradient(ellipse at 30% 20%, var(--sun) 0 18%, transparent 40%),
                radial-gradient(ellipse at 75% 60%, var(--sun) 0 15%, transparent 38%),
                radial-gradient(ellipse at 20% 75%, var(--sun) 0 12%, transparent 35%),
                var(--orange); }
  .masthead { position: absolute; left: 0; top: 0; width: 927px; height: 98px; background: var(--white); }
  .tagline { position: absolute; top: 22px; font-family: "Francois One", sans-serif; font-size: 40px; line-height: 1; white-space: nowrap; transform: scaleY(1.25); transform-origin: left top; }
  .tagline.greener { left: 8px; color: var(--green); }
  .tagline.smarter { left: 218px; color: var(--purple); }
  .tagline.closer { left: 428px; color: var(--yellow); }
  .brand { position: absolute; left: 592px; top: 6px; width: 335px; height: 90px; }
  .brand-mark { position: absolute; left: 14px; top: 8px; width: 50px; height: 50px; border-radius: 50%; background: var(--orange); }
  .brand-note { position: absolute; left: 72px; top: 24px; font-size: 14px; color: var(--ink); white-space: nowrap; }
  .brand-name { position: absolute; left: 62px; top: 64px; font-size: 17px; color: var(--slate); font-weight: 700; }
  .brand-line { position: absolute; left: 154px; top: 64px; font-size: 17px; color: var(--slate); white-space: nowrap; }
  .band { position: absolute; left: 0; top: 98px; width: 927px; height: 15px; background: var(--grey-band); }
  .panel { position: absolute; background: var(--brown); border: 3px solid var(--white); border-radius: 8px; color: var(--white); }
  .panel h2 { font-family: "Audiowide", sans-serif; font-weight: 400; color: var(--yellow); font-size: 21px; line-height: 26px; }
  .panel p, .panel li { font-weight: 700; font-size: 16.5px; line-height: 21.7px; }
  .who { left: -6px; top: 136px; width: 401px; height: 308px; padding: 6px 34px 0 16px; border-left: 0; border-radius: 0 8px 8px 0; }
  .who h2 { margin-bottom: 4px; }
  .safe { left: 494px; top: 345px; width: 440px; height: 361px; padding: 8px 40px 0 16px; border-right: 0; }
  .safe h2 { margin-bottom: 12px; }
  .safe ul { list-style: none; padding-left: 6px; }
  .safe li { padding-left: 26px; text-indent: -17px; }
  .safe li::before { content: "-  "; }
  .quality { left: -6px; top: 760px; width: 401px; height: 128px; padding: 4px 34px 0 16px; border-left: 0; border-radius: 0 8px 8px 0; }
  .quality h2 { margin-bottom: 3px; }
  .quality p { line-height: 21px; }
  .contact { position: absolute; left: 553px; top: 729px; width: 374px; height: 154px; background: var(--slate); border: 3px solid var(--white); border-right: 0; color: var(--white); text-align: center; padding-top: 10px; font-style: normal; }
  .contact .contact-name { font-size: 27px; letter-spacing: 1px; margin-bottom: 2px; }
  .contact p { font-weight: 700; font-size: 19px; line-height: 25px; }
  .photo { position: absolute; border: 4px solid var(--white); border-radius: 4px; }
  .photo-award { left: 412px; top: 127px; width: 198px; height: 203px; background: linear-gradient(160deg, #d9d2c4, #3b3630 70%); }
  .photo-booth { left: 641px; top: 127px; width: 276px; height: 203px; background: linear-gradient(170deg, #e4e0a0, #8a8a7a 55%, #3a3a3a); }
  .photo-desk { left: 59px; top: 912px; width: 262px; height: 278px; background: linear-gradient(180deg, #6b7a5a, #c84a3a 40%, #eeeeee 60%, #f7f7f7); }
  .module { position: absolute; }
  .module-mono { left: 31px; top: 469px; width: 170px; height: 278px; background: linear-gradient(180deg, #2a2d33, #14161a); border: 3px solid #b9b9b9; }
  .module-poly { left: 218px; top: 474px; width: 173px; height: 273px; background: linear-gradient(180deg, #3a5fa8, #1e3c80); border: 3px solid #b9b9b9; }
  .events { left: 391px; top: 912px; width: 540px; height: 278px; padding: 2px 0 0 14px; border-right: 0; }
  .events h2 { font-size: 21px; }
  .events .intro { font-size: 16px; line-height: 20px; margin: 0 0 3px; }
  .events table { width: 498px; border-collapse: collapse; background: var(--white); color: var(--ink); }
  .events th, .events td { border: 1px solid #555; font-size: 12px; text-align: left; padding: 1px 2px; height: 19.5px; }
  .events th { font-weight: 700; }
</style>
</head>
<body>
<main class="ad">
  <header class="masthead">
    <span class="tagline greener">GREENER.</span>
    <span class="tagline smarter">SMARTER.</span>
    <span class="tagline closer">CLOSER.</span>
    <div class="brand">
      <span class="brand-mark"></span>
      <span class="brand-note">LOGO PLACEHOLDER ONLY</span>
      <span class="brand-name">Sunvera</span>
      <span class="brand-line">Delivering safe solar</span>
    </div>
  </header>
  <div class="band"></div>

  <section class="panel who">
    <h2>Who is Sunvera?</h2>
    <p>A leading international solar module developer and producer, offering the solar industry’s best quality / price ratio in the global PV market. Sunvera produces high quality, reliable solar modules backed by a world-class warranty, at competitive prices. Headquartered in Shanghai, Sunvera has offices throughout Asia, Europe and North America to support an international customer-base, providing on-site technical support, customer service and product development teams.</p>
  </section>

  <div class="photo photo-award" role="img" aria-label="Company representative holding a solar industry award"></div>
  <div class="photo photo-booth" role="img" aria-label="Team toasting at the company exhibition booth"></div>

  <section class="panel safe">
    <h2>Delivering Safe Solar</h2>
    <p>The folks at Sunvera have focused their efforts on solar PV, because they believe this to be the best way to harvest energy from the sun. The collection of energy, the use of modules, and the returns on investments even after years of product use all contribute to the concept of "Safe Solar." With its strong sales and technical support staff, Sunvera is sure to deliver safe solar to their customers - each and every day.</p>
    <ul>
      <li>Energy from a safe source</li>
      <li>A safe investment – purchasing a product that is built to last 20+ years</li>
      <li>A safe product (no moving parts, limited impact on the environment)</li>
    </ul>
  </section>

  <div class="module module-mono" role="img" aria-label="Monocrystalline solar module"></div>
  <div class="module module-poly" role="img" aria-label="Polycrystalline solar module"></div>

  <section class="panel quality">
    <h2>Quality Products</h2>
    <p>Sunvera offers a wide range of monocrystalline and polycrystalline solar modules for residential, commercial, utility and large scale projects.</p>
  </section>

  <address class="contact">
    <div class="contact-name">Sunvera</div>
    <p>1234 Streetname Ave.</p>
    <p>City, State 01234</p>
    <p>(123) 456 - 7890</p>
    <p>www.website.com</p>
  </address>

  <div class="photo photo-desk" role="img" aria-label="Exhibition reception desk with red flower arrangement"></div>

  <section class="panel events">
    <h2>Learn More About Us In Person!</h2>
    <p class="intro">Visit the Sunvera team at any of the following exhibitions.</p>
    <table>
      <tr><th>Name</th><th>Date</th><th>City</th><th>Country</th><th>Booth No.</th></tr>
      <tr><td>CLIMAFAIR</td><td>Feb 7-10</td><td>Paris</td><td>France</td><td>Hall 7.2, J58</td></tr>
      <tr><td>PV WORLD Tokyo</td><td>Feb 29 - Mar 2</td><td>Tokyo</td><td>Japan</td><td>E41-33</td></tr>
      <tr><td>ECOFORUM</td><td>Mar 15-18</td><td>Athens</td><td>Greece</td><td>Hall 4</td></tr>
      <tr><td>PV STATES</td><td>Mar 19-21</td><td>San Jose</td><td>USA</td><td>Booth #1015</td></tr>
      <tr><td>BUILDGREEN</td><td>Mar 20-22</td><td>London</td><td>UK</td><td>N3165</td></tr>
      <tr><td>SEF</td><td>Mar 29-31</td><td>Stuttgart</td><td>Germany</td><td>4E19</td></tr>
      <tr><td>ENVI</td><td>Apr 3-5</td><td>Paris</td><td>France</td><td>Hall 1 Stand L33</td></tr>
      <tr><td>SUNSHOW</td><td>May 9-11</td><td>Verona</td><td>Italy</td><td>Hall 6, E2.2</td></tr>
      <tr><td>SOLCON</td><td>May 16-18</td><td>Shanghai</td><td>China</td><td>E1-550</td></tr>
      <tr><td>SUNFORUM</td><td>Jun 13-15</td><td>Munich</td><td>Germany</td><td>A3.360</td></tr>
    </table>
  </section>
</main>
</body>
</html>
```